Letterhead design - Harwick Group

We have just had our Logo created and our now wantng a letterhead design to incorporate this. Please use the same colours as in the logo, which is attached.
Please use the company details below
P O Box 86, Bleneheim 7315
Ph: 03 642 1937
dave@harwickgroup.co.nz
We would like a professional look
We need an overall letterhead design for our varied group of buisinesses which are based in NZ and overseas. We grow and develop buisinesses. Our companies began in NZ but we now have branches overseas as well. People are our greatest asset and we employ some incredible staff. Our buisinesses are scientific, innovative and growing in size and expertise with a financial base.

Target Market(s)

Professionals

Industry/Entity Type

Investment

Requirements
Must have
• Easy to read.
• Please use the same colours as in the logo
• Please use the company details below
• P O Box 86, Bleneheim 7315
• Ph: 03 642 1937
• dave@harwickgroup.co.nz

```html
<!DOCTYPE html>
<html lang="en">
<head>
<meta charset="utf-8">
<title>Harwick Group Letterhead</title>
<link rel="stylesheet" href="https://fonts.googleapis.com/css2?family=Open+Sans:wght@400;600;700&display=swap">
<style>
  :root {
    --brand-green: #24b36f;
    --brand-grey: #555a5c;
    --text-dark: #3a3a3a;
    --paper: #ffffff;
    --backdrop: #e4eaeb;
    --watermark: rgba(85, 90, 92, 0.09);
  }
  * { box-sizing: border-box; margin: 0; padding: 0; }
  html, body {
    width: 1131px;
    height: 1200px;
    overflow: hidden;
    background: var(--backdrop);
    font-family: "Open Sans", Arial, sans-serif;
  }
  .letterhead {
    position: absolute;
    left: 165px;
    top: 35px;
    width: 800px;
    height: 1130px;
    background: var(--paper);
    box-shadow: 0 4px 14px rgba(0, 0, 0, 0.18);
    overflow: hidden;
  }
  .top-band {
    position: absolute;
    left: 0; top: 0;
    width: 100%;
    height: 16px;
    background: var(--brand-green);
  }
  .bottom-band {
    position: absolute;
    left: 0; bottom: 0;
    width: 100%;
    height: 24px;
    background: var(--brand-green);
  }
  .brand {
    position: absolute;
    left: 36px;
    top: 46px;
    display: flex;
    align-items: center;
    gap: 10px;
  }
  .brand-mark {
    width: 26px;
    height: 26px;
    background: var(--brand-grey);
  }
  .brand-name {
    font-size: 24px;
    font-weight: 700;
    color: var(--brand-green);
    letter-spacing: 0.5px;
    text-transform: uppercase;
  }
  .contact {
    position: absolute;
    left: 36px;
    top: 92px;
    font-size: 12px;
    line-height: 17px;
  }
  .contact .address,
  .contact .email { color: var(--brand-green); }
  .contact .phone { color: var(--text-dark); }
  .page-title {
    position: absolute;
    right: 36px;
    top: 150px;
    width: 200px;
    text-align: left;
  }
  .page-title-text {
    font-size: 17px;
    font-weight: 700;
    color: var(--brand-green);
    text-transform: uppercase;
    padding-bottom: 5px;
    border-bottom: 2px solid var(--brand-grey);
    white-space: nowrap;
  }
  .watermark {
    position: absolute;
    left: 0;
    top: 520px;
    width: 100%;
    text-align: center;
    font-size: 56px;
    font-weight: 700;
    color: var(--watermark);
    text-transform: uppercase;
    letter-spacing: 2px;
  }
</style>
</head>
<body>
  <main class="letterhead">
    <div class="top-band"></div>

    <header class="brand">
      <span class="brand-mark"></span>
      <span class="brand-name">Harwick Group</span>
    </header>

    <address class="contact" style="font-style: normal;">
      <div class="address">PO: Box 86, Bleneheim 7315</div>
      <div class="phone">Phone: 03 642 1937</div>
      <div class="email">Email:dave@harwickgroup.co.nz</div>
    </address>

    <div class="page-title">
      <div class="page-title-text">Harwick Group</div>
    </div>

    <div class="watermark" aria-hidden="true">Harwick Group</div>

    <div class="bottom-band"></div>
  </main>
</body>
</html>
```